Clean invitation for a wedding

Design a wedding invitation.
Those examples in attachment. They are looking for this style, about the same construction. Back with the symbols etc.

Clean sleek design.

marriage name:
Kemp & Rosetta
02.06.23

You can copy the rest of the texts from the examples.

```html
<!DOCTYPE html>
<html lang="en">
<head>
<meta charset="UTF-8">
<title>Kemp &amp; Rosetta – Wedding Invitation</title>
<link rel="stylesheet" href="https://fonts.googleapis.com/css2?family=Yellowtail&family=Libre+Baskerville&family=Montserrat:wght@500;600&display=block">
<style>
  :root {
    --backdrop: #4a4946;
    --paper: #efebdc;
    --ink: #2f2e2c;
    --icon-tone: #d9d4c2;
  }
  * { margin: 0; padding: 0; box-sizing: border-box; }
  html, body { width: 1200px; height: 864px; overflow: hidden; }
  body { background: var(--backdrop); position: relative; color: var(--ink); }

  .card {
    position: absolute;
    top: 54px;
    width: 540px;
    height: 756px;
    background: var(--paper);
  }
  .card--invite { left: 44px; }
  .card--program { left: 617px; }

  .line {
    position: absolute;
    left: 0; right: 0;
    text-align: center;
    white-space: nowrap;
    font-weight: normal;
  }
  .caps {
    font-family: "Montserrat", sans-serif;
    font-weight: 600;
    text-transform: uppercase;
    letter-spacing: 0.16em;
  }
  .serif {
    font-family: "Libre Baskerville", serif;
    letter-spacing: 0.12em;
  }

  .intro { top: 66px; font-size: 10.5px; line-height: 19px; }

  .names {
    font-family: "Yellowtail", "Brush Script MT", cursive;
    overflow: hidden;
  }
  .names--first  { top: 102px; height: 124px; font-size: 116px; line-height: 124px; }
  .names--amp    { top: 218px; height: 76px;  font-size: 74px;  line-height: 76px; }
  .names--second { top: 268px; height: 124px; font-size: 116px; line-height: 124px; }

  .date { top: 438px; font-size: 42px; line-height: 44px; }
  .time { top: 488px; font-size: 10px; line-height: 14px; }
  .venue { top: 526px; font-size: 10.5px; line-height: 14px; }
  .city { top: 543px; font-size: 7.5px; line-height: 10px; }
  .divider {
    position: absolute;
    top: 576px; left: 256px;
    width: 28px; height: 2px;
    background: var(--ink);
  }
  .rsvp-title { top: 600px; font-size: 34px; line-height: 40px; }
  .rsvp-note { top: 655px; font-size: 10px; line-height: 17px; }

  .program-title { top: 60px; font-size: 32px; line-height: 40px; letter-spacing: 0.16em; }

  .timeline {
    position: absolute;
    left: 269px; top: 175px;
    width: 2px; height: 465px;
    background: var(--ink);
  }
  .event { position: absolute; left: 0; width: 540px; }
  .event__icon {
    position: absolute;
    left: 128px; top: -27px;
    width: 54px; height: 54px;
    border-radius: 8px;
    background: var(--icon-tone);
  }
  .event__marker {
    position: absolute;
    left: 265px; top: -5px;
    width: 10px; height: 10px;
    background: var(--ink);
    transform: rotate(45deg);
  }
  .event__text {
    position: absolute;
    left: 300px; width: 160px;
    top: -13px;
    text-align: center;
    font-size: 10px;
    line-height: 13px;
  }
</style>
</head>
<body>

<section class="card card--invite">
  <p class="line caps intro">Please join us to<br>celebrate the wedding of</p>
  <h1 class="line names names--first">Kemp</h1>
  <p class="line names names--amp">&amp;</p>
  <p class="line names names--second">Rosetta</p>
  <p class="line serif date">02.06.23</p>
  <p class="line caps time">1O'clock in the afternoon</p>
  <p class="line caps venue">At Cedar Hollow Estate</p>
  <p class="line caps city">Malibu California</p>
  <span class="divider"></span>
  <h2 class="line serif rsvp-title">RSVP</h2>
  <p class="line caps rsvp-note">Kindly RSVP to Kemp by May 30th 2023<br>kemprosettawedding@email.com</p>
</section>

<section class="card card--program">
  <h2 class="line serif program-title">PROGRAM</h2>
  <span class="timeline"></span>

  <div class="event" style="top:175px">
    <div class="event__icon" role="img" aria-label="Icon of two wedding rings"></div>
    <span class="event__marker"></span>
    <p class="event__text caps">13:30<br>Wedding</p>
  </div>
  <div class="event" style="top:268px">
    <div class="event__icon" role="img" aria-label="Icon of two champagne glasses toasting"></div>
    <span class="event__marker"></span>
    <p class="event__text caps">15:00<br>Snacks &amp; Drinks</p>
  </div>
  <div class="event" style="top:361px">
    <div class="event__icon" role="img" aria-label="Icon of a tiered wedding cake"></div>
    <span class="event__marker"></span>
    <p class="event__text caps">16:00<br>Wedding Cake</p>
  </div>
  <div class="event" style="top:454px">
    <div class="event__icon" role="img" aria-label="Icon of a plate with fork and knife"></div>
    <span class="event__marker"></span>
    <p class="event__text caps">17:30<br>Dinner</p>
  </div>
  <div class="event" style="top:547px">
    <div class="event__icon" role="img" aria-label="Icon of a bride and groom dancing"></div>
    <span class="event__marker"></span>
    <p class="event__text caps" style="top:-18px">19:00<br>Bride &amp; Groom<br>Dance</p>
  </div>
  <div class="event" style="top:640px">
    <div class="event__icon" role="img" aria-label="Icon of music notes"></div>
    <span class="event__marker"></span>
    <p class="event__text caps">20:30<br>Reception Party</p>
  </div>
</section>

</body>
</html>
```